Presentation card Venture KELO - Tech Incubator from Perú

We need a Design to promote the incubator of technology Startups.
We are in Perú, we work with a string tech filter and develop enterprenurship competencies in the Startup team.
The card is to facilitators and staff memebers of VentureKELO.
We want a clear, modern, tech and agile Design.

We work to help New enterprises of technology here in Perú, we expect the candidates have a big competencies to Research and develop technological products.

We work using methodologies from QRB, Folmestry, Brakewell and Harrowgate univeesities. Our book base is the disciplina of enterpreneur.

We work events all year using diferent formats: Brightforge, Vorne price, OPRA Model Competition you can use these logros in your Design.

Set the name, role, email, cell phone number, address.

Example:
// Contact info section
Tobías Quiroveda
Swift Modeling Hub Manager
tobias.quiroveda@kelo-example.pe
(511) 999 000 417

// Address info section
VentureKELO
Technology-based business incubator
Av. Los Cedrales 884, Valdora
Lima - Perú
web: venture-kelo-example.org.pe
email: venture@kelo-example.pe
phone number: (511) 3926508 ext. 4418

// (optional)Lema section
Making happy using technology

// Social network section
facebook: venturekelooficial

Target Market(s)

Enterprenurship, CTO, Investors, Companies interested on open innovation services

Industry/Entity Type

Information Technology

Contact Information for Business Card

Name, Role, Email, Cell phone number

Colors

Designer to choose colors to be used in the design.

Requirements
Must have
• Logo forms and colors
Nice to have
• I add pictures of the leaders of incubator
Should not have
• No vertical designs

```html
<!DOCTYPE html>
<html lang="es">
<head>
<meta charset="utf-8">
<title>Venture KELO – Business Card</title>
<link href="https://fonts.googleapis.com/css2?family=Oswald:wght@500&family=Work+Sans:wght@400;800&display=swap" rel="stylesheet">
<style>
  :root {
    --backdrop: #161616;
    --card: #232323;
    --card-edge: #2c2c2c;
    --accent: #c2406a;
    --ink: #f4f4f4;
    --ink-soft: #d8d8d8;
  }
  * { box-sizing: border-box; margin: 0; padding: 0; }
  html, body {
    width: 1200px; height: 900px; overflow: hidden;
    background: var(--backdrop);
    font-family: "Work Sans", sans-serif;
  }
  .canvas {
    width: 1200px; height: 900px;
    display: flex; flex-direction: column; align-items: center; justify-content: center;
    gap: 36px;
    background: radial-gradient(ellipse at 60% 40%, #2a2a2a 0%, var(--backdrop) 70%);
  }
  .card {
    position: relative;
    width: 700px; height: 400px;
    background: linear-gradient(135deg, var(--card) 0%, var(--card-edge) 100%);
    border-radius: 4px;
    box-shadow: 0 18px 40px rgba(0,0,0,.55);
  }
  /* Front */
  .brand {
    position: absolute; top: 50%; left: 50%;
    transform: translate(-50%, -50%);
    display: flex; align-items: center; gap: 18px;
    white-space: nowrap;
  }
  .brand-mark {
    width: 30px; height: 30px; background: var(--accent); flex: none;
  }
  .brand-name {
    font-weight: 800; font-size: 50px; letter-spacing: 1px;
    color: var(--ink); line-height: 1; white-space: nowrap;
  }
  /* Back */
  .identity {
    position: absolute; top: 150px; right: 390px;
    text-align: right;
  }
  .person-name {
    font-family: "Oswald", sans-serif; font-weight: 500;
    font-size: 32px; letter-spacing: 1px; text-transform: uppercase;
    color: var(--accent); line-height: 1.15; white-space: nowrap;
  }
  .person-role {
    font-size: 16px; color: var(--ink-soft); letter-spacing: 1px; margin-top: 4px;
  }
  .divider {
    position: absolute; left: 330px; top: 156px;
    width: 2px; height: 70px; background: var(--ink-soft);
  }
  .contact-list {
    position: absolute; left: 350px; top: 156px;
    list-style: none;
  }
  .contact-item {
    display: flex; align-items: center; gap: 10px;
    font-size: 15px; letter-spacing: .3px; color: var(--ink);
    line-height: 24px; white-space: nowrap;
  }
  .contact-icon { width: 12px; height: 12px; flex: none; }
  .address {
    position: absolute; left: 70px; bottom: 58px;
    font-size: 18px; letter-spacing: 1px; color: var(--ink);
    white-space: nowrap;
  }
</style>
</head>
<body>
<main class="canvas">
  <section class="card card-front">
    <div class="brand">
      <span class="brand-mark"></span>
      <span class="brand-name">Venture KELO</span>
    </div>
  </section>

  <section class="card card-back">
    <div class="identity">
      <p class="person-name">Tobías Quiroveda</p>
      <p class="person-role">Director</p>
    </div>
    <div class="divider"></div>
    <ul class="contact-list">
      <li class="contact-item">
        <svg class="contact-icon" viewBox="0 0 16 16"><path d="M4 1l3 3-2 2c1 2 3 4 5 5l2-2 3 3-2 3C7 15 1 9 1 3z" fill="none" stroke="#c2406a" stroke-width="1.5"/></svg>
        (511) 999 000 417
      </li>
      <li class="contact-item">
        <svg class="contact-icon" viewBox="0 0 16 16"><rect x="1" y="3" width="14" height="10" fill="none" stroke="#c2406a" stroke-width="1.5"/><path d="M1 3l7 6 7-6" fill="none" stroke="#c2406a" stroke-width="1.5"/></svg>
        tobias.quiroveda@kelo-example.pe
      </li>
      <li class="contact-item">
        <svg class="contact-icon" viewBox="0 0 16 16"><circle cx="8" cy="8" r="6.5" fill="none" stroke="#c2406a" stroke-width="1.3"/><ellipse cx="8" cy="8" rx="3" ry="6.5" fill="none" stroke="#c2406a" stroke-width="1.1"/><path d="M1.5 8h13" stroke="#c2406a" stroke-width="1.1"/></svg>
        venture-kelo-example.org.pe
      </li>
    </ul>
    <p class="address">Av. Los Cedrales 884, Valdora, Lima - Perú</p>
  </section>
</main>
</body>
</html>
```